AUSTRALIAN CONSULTING FIRM BUSINESS CARD - MODERN

We are wanting a modern, clean lined business card design. We are professional niche consultancy firm situated in Australia called Marlow Advisory Partners Pty Ltd.
The card should communicate professionalism and creativity and draw on our logo design (attached).
The design should be two sided, landscape orientation.
Target Market(s)
government, not for profit sector, corporate clients
Industry/Entity Type
Landscape
Requirements
Must have
- logo
no new introduced colours

```html
<!DOCTYPE html>
<html lang="en">
<head>
<meta charset="utf-8">
<title>Marlow Advisory Partners – Business Card</title>
<link rel="stylesheet" href="https://fonts.googleapis.com/css2?family=Quicksand:wght@500;700&display=swap">
<style>
  :root {
    --brand-blue: #1b1bd8;
    --brand-purple: #a42ed6;
    --brand-green: #8fe33c;
    --brand-cyan: #3cd2f2;
    --pastel-green: #ddf5c2;
    --pastel-purple: #dcc0f2;
    --pastel-blue: #bfe4fb;
    --stone-dark: #a3a5a6;
    --stone-light: #eef0f0;
    --ink: #1d1d1d;
    --paper: #ffffff;
  }
  html, body {
    margin: 0;
    padding: 0;
    width: 1200px;
    height: 329px;
    overflow: hidden;
    background: var(--paper);
  }
  .card-spread {
    position: relative;
    width: 1200px;
    height: 329px;
    font-family: "Quicksand", "Trebuchet MS", sans-serif;
    color: var(--ink);
  }

  /* Front side */
  .card-front {
    position: absolute;
    left: 0;
    top: 0;
    width: 592px;
    height: 329px;
    background:
      radial-gradient(ellipse 60% 45% at 50% 42%, var(--stone-light) 0%, rgba(238,240,240,0) 100%),
      linear-gradient(180deg, var(--stone-dark) 0%, #c9cbcb 45%, var(--stone-dark) 100%);
  }
  .front-brand {
    position: absolute;
    left: 72px;
    top: 112px;
    display: flex;
    align-items: center;
    gap: 22px;
  }
  .brand-dot {
    width: 70px;
    height: 70px;
    border-radius: 50%;
    background: var(--brand-cyan);
    flex: none;
  }
  .brand-name {
    color: var(--brand-blue);
    font-weight: 700;
    line-height: 1;
  }
  .front-brand .brand-name-main {
    display: block;
    font-size: 66px;
    letter-spacing: 1px;
  }
  .front-brand .brand-name-sub {
    display: block;
    font-size: 19px;
    margin-top: 8px;
    letter-spacing: 0.3px;
  }

  /* Back side */
  .card-back {
    position: absolute;
    left: 592px;
    top: 0;
    width: 608px;
    height: 329px;
    background: var(--paper);
  }
  .back-brand {
    position: absolute;
    left: 30px;
    top: 30px;
  }
  .back-brand .brand-name-main {
    display: block;
    font-size: 40px;
    letter-spacing: 1px;
  }
  .back-brand .brand-name-sub {
    display: block;
    font-size: 12.5px;
    margin-top: 4px;
  }
  .contact-name {
    position: absolute;
    left: 30px;
    top: 110px;
    margin: 0;
    font-size: 27px;
    font-weight: 500;
    letter-spacing: 0.5px;
  }
  .contact-role {
    position: absolute;
    left: 30px;
    top: 146px;
    margin: 0;
    font-size: 21px;
    font-weight: 500;
    letter-spacing: 0.3px;
  }
  .contact-list {
    position: absolute;
    left: 30px;
    top: 214px;
    margin: 0;
    padding: 0;
    list-style: none;
    font-size: 20.5px;
    font-weight: 500;
    line-height: 33px;
    letter-spacing: 0.3px;
  }
  .contact-label {
    font-weight: 700;
  }
  .back-accent {
    position: absolute;
    right: 0;
    top: 0;
    width: 330px;
    height: 329px;
    background:
      radial-gradient(circle at 30% 10%, var(--pastel-green) 0%, rgba(221,245,194,0) 45%),
      radial-gradient(circle at 35% 45%, var(--pastel-purple) 0%, rgba(220,192,242,0) 50%),
      radial-gradient(circle at 60% 75%, var(--pastel-blue) 0%, rgba(191,228,251,0) 55%),
      linear-gradient(90deg, rgba(255,255,255,0) 0%, rgba(191,228,251,0.35) 100%);
  }
</style>
</head>
<body>
  <main class="card-spread">
    <section class="card-front" aria-label="Card front">
      <div class="front-brand">
        <span class="brand-dot" aria-hidden="true"></span>
        <div class="brand-name">
          <span class="brand-name-main">MARLOW</span>
          <span class="brand-name-sub">ADVISORY PARTNERS PTY LTD</span>
        </div>
      </div>
    </section>

    <section class="card-back" aria-label="Card back">
      <div class="back-accent" role="img" aria-label="Soft pastel arcs and circles in green, purple and blue as brand decoration"></div>
      <div class="back-brand brand-name">
        <span class="brand-name-main">MARLOW</span>
        <span class="brand-name-sub">ADVISORY PARTNERS PTY LTD</span>
      </div>
      <h1 class="contact-name">Owen Harte</h1>
      <p class="contact-role">Marketing Manager</p>
      <ul class="contact-list">
        <li><span class="contact-label">P:</span> +61 (3) 9555 0182</li>
        <li><span class="contact-label">F:</span> +61 (3) 9555 0196</li>
        <li><span class="contact-label">E:</span> owen@marlowadvisorypartners.com</li>
      </ul>
    </section>
  </main>
</body>
</html>
```